Need help in designing new business card utilizing our new logo.

Veltrix Solutions works with Construction Business Owners, Managers & IT Professionals to strengthen software usage and increase user productivity.

Our Construction Accounting and Mobile Field Management Software Clients engage with us in the following areas:

New Software Implementations
Software Re-Implementations
Redesigning Software Usage at the User Level
Project Coordination & Management
Continued Software Support

Old tag line:
Clear Choices - Working Systems

www.veltrix-solutions.example

Quad Shift is a product, but not needed for a new business card.

```html
<!DOCTYPE html>
<html lang="en">
<head>
<meta charset="utf-8">
<title>Veltrix Solutions – Business Card</title>
<link href="https://fonts.googleapis.com/css2?family=Roboto:wght@400;500;700&family=Roboto+Condensed:wght@700&display=swap" rel="stylesheet">
<style>
  :root {
    --brand-blue: #0c17a6;
    --brand-blue-deep: #08108a;
    --band-grey: #bdbdc0;
    --band-grey-light: #d6d6d8;
    --paper: #f1f1f1;
    --ink: #1b1b1f;
    --white: #ffffff;
    --stage: #bfbfbf;
  }
  * { box-sizing: border-box; margin: 0; padding: 0; }
  html, body { width: 1200px; height: 576px; overflow: hidden; }
  body {
    background: var(--stage);
    font-family: "Roboto", Arial, sans-serif;
    position: relative;
  }
  .card {
    position: absolute;
    top: 138px;
    width: 484px;
    height: 294px;
    border-radius: 12px;
    overflow: hidden;
  }
  /* Front */
  .card-front {
    left: 82px;
    background: linear-gradient(160deg, var(--brand-blue) 0%, var(--brand-blue-deep) 100%);
    color: var(--white);
  }
  .front-brand {
    position: absolute;
    top: 62px;
    left: 0; right: 0;
    display: flex;
    justify-content: center;
    align-items: center;
    gap: 14px;
  }
  .brand-square {
    width: 40px; height: 40px;
    background: var(--white);
  }
  .brand-name {
    font-weight: 500;
    line-height: 1;
    text-transform: uppercase;
  }
  .front-brand .brand-name { font-size: 34px; color: var(--white); }
  .front-brand .brand-name span { display: block; font-size: 17px; letter-spacing: 7px; margin-top: 4px; }
  .services-band {
    position: absolute;
    top: 167px;
    left: 0; right: 0;
    height: 80px;
    background: linear-gradient(90deg, var(--band-grey) 0%, var(--band-grey-light) 50%, var(--band-grey) 100%);
    color: var(--ink);
    font-size: 13.4px;
    line-height: 18.5px;
    text-align: center;
    padding-top: 12px;
  }
  .services-band .sep { margin: 0 9px; }
  .front-web {
    position: absolute;
    top: 262px;
    left: 0; right: 0;
    display: flex;
    justify-content: center;
    align-items: center;
    gap: 18px;
    font-size: 12px;
  }
  .front-web .rule { width: 34px; height: 1px; background: rgba(255,255,255,0.7); }

  /* Back */
  .card-back { left: 602px; background: var(--paper); }
  .back-shape { position: absolute; inset: 0; }
  .back-brand {
    position: absolute;
    left: 0; width: 216px;
    top: 112px;
    text-align: center;
  }
  .back-brand .brand-square {
    width: 36px; height: 36px;
    background: var(--brand-blue);
    margin: 0 auto 10px;
  }
  .back-brand .brand-name { font-size: 31px; color: var(--brand-blue); }
  .back-brand .brand-name span { display: block; font-size: 15px; letter-spacing: 6px; margin-top: 3px; }
  .contact {
    position: absolute;
    left: 252px;
    top: 48px;
    color: var(--white);
    font-size: 12.5px;
    line-height: 17px;
    white-space: nowrap;
  }
  .contact-name {
    font-family: "Roboto Condensed", "Arial Narrow", sans-serif;
    font-weight: 700;
    font-size: 21px;
    line-height: 24px;
  }
  .contact-role { margin-bottom: 16px; }
  .contact-address { margin-bottom: 10px; }
  .contact-line { display: flex; align-items: center; gap: 10px; }
  .contact-line svg { width: 11px; height: 11px; flex: none; }
  .tagline-band {
    position: absolute;
    left: 200px; right: 0;
    top: 253px;
    height: 18px;
    background: linear-gradient(90deg, var(--band-grey) 0%, var(--band-grey-light) 60%, var(--band-grey) 100%);
    color: var(--ink);
    font-size: 12.5px;
    line-height: 18px;
    padding-left: 26px;
    white-space: nowrap;
  }
</style>
</head>
<body>

<section class="card card-front" aria-label="Card front">
  <div class="front-brand">
    <div class="brand-square"></div>
    <div class="brand-name">Veltrix<span>Solutions</span></div>
  </div>
  <div class="services-band">
    <p>New Software Implementations<span class="sep">|</span>Software Re-Implementations</p>
    <p>Redesigning Software Usage at the User Level</p>
    <p>Project Coordination &amp; Management<span class="sep">|</span>Continued Software Support</p>
  </div>
  <div class="front-web">
    <span class="rule"></span>
    <span>www.veltrix-solutions.example</span>
    <span class="rule"></span>
  </div>
</section>

<section class="card card-back" aria-label="Card back">
  <svg class="back-shape" viewBox="0 0 484 294" preserveAspectRatio="none" aria-hidden="true">
    <path d="M186 0 C232 70 236 220 208 294 L484 294 L484 0 Z" fill="#0c17a6"/>
    <path d="M178 0 C224 70 226 220 196 294 L208 294 C236 220 232 70 186 0 Z" fill="#b4b4b7"/>
  </svg>
  <div class="back-brand">
    <div class="brand-square"></div>
    <div class="brand-name">Veltrix<span>Solutions</span></div>
  </div>
  <div class="contact">
    <p class="contact-name">Dana R. Whitfield</p>
    <p class="contact-role">Owner</p>
    <p class="contact-address">48B Harbor Lane - Suite 112<br>Riverton, NY 12000</p>
    <p class="contact-line">
      <svg viewBox="0 0 12 12" aria-hidden="true"><rect x="3" y="0.5" width="6" height="11" rx="1.2" fill="none" stroke="#fff" stroke-width="1.2"/><rect x="5" y="9" width="2" height="1" fill="#fff"/></svg>
      555-014-2837</p>
    <p class="contact-line">
      <svg viewBox="0 0 12 12" aria-hidden="true"><path d="M1 4 Q6 0 11 4 L10 5.5 L8 5 L8 4 Q6 3 4 4 L4 5 L2 5.5 Z" fill="#fff"/><rect x="2.5" y="6" width="7" height="5" rx="1" fill="#fff"/></svg>
      555-018-4420 ext. 100</p>
    <p class="contact-line">
      <svg viewBox="0 0 12 12" aria-hidden="true"><rect x="0.5" y="2" width="11" height="8" fill="#fff"/><path d="M0.5 2 L6 7 L11.5 2" fill="none" stroke="#0c17a6" stroke-width="1"/></svg>
      dana@veltrix-solutions.example</p>
    <p class="contact-line">
      <svg viewBox="0 0 12 12" aria-hidden="true"><circle cx="6" cy="6" r="5.2" fill="none" stroke="#fff" stroke-width="1"/><ellipse cx="6" cy="6" rx="2.3" ry="5.2" fill="none" stroke="#fff" stroke-width="0.9"/><line x1="0.8" y1="6" x2="11.2" y2="6" stroke="#fff" stroke-width="0.9"/></svg>
      www.veltrix-solutions.example</p>
  </div>
  <div class="tagline-band">Clear Choices - Working Systems</div>
</section>

</body>
</html>
```